Business Card & Logo Design - Hedge Fund

We need a business card and logo design for a hedge fund. The hedge fund is named Morvane Equity LLC. Morvane Equity was created by finance professors and the strategy is based academic research that looks for patterns in stock prices. The design should look conservative, solid, strong. We favor a classic style - nothing flashy. The logo can relate to the name Morvane Equity, or it could involve a symbol design that connotes "science" . We are open to ideas. We do not want alot of colors - but if any, color - blue is preferred. The font that seems to look best for the name (Morvane Equity) is arial black. We are open to ideas. Most important - we want to see a mock up of an actual business card with the logo concept embedded. The business card should include space for : company name, individual name, position title, cell phone, address. We hope to have this work done by Sept. 8.

Target Market(s)

We will be meeting with and giving the business card to institutions and high net worth individuals.

Industry/Entity Type

Investment Advisory

Contact Information for Business Card

Company name - Morvane Equity LLC
Individual name - Peter Dalby
Title - Portfolio Manager
Cell - (412) 555-0187
Address - 2650 Birchmont Lane, Suite 300, Atlanta GA 30327

Font styles to use
Other font styles liked:
• Arial

Colors
3277b5
0255a3
85acd3
cedeed
fdf9cf
d9d9d9
e6e6e6
f04a50
6b449b

Requirements
Must have
• Must have card details that are sited above.
• We would like a logo related to the name (Morvane Equity) or concept of the fund.
Nice to have
• We want conservative / understated / clean crisp look.
• If any colors - we prefer conservative appearance - blue / gray.
• I have enclosed an example of a card style that looks attractive - please do not exactly copy this card. This is not our company or logo. I feel the layout is attractive - just as an example
Should not have
• Avoid too much color.
• I have selected some preferred colors. Please do not use all of the colors - I have selected a few that might work - but I am not sure. We are open to your ideas so please do not feel the need to use all or any of these.

```html
<!DOCTYPE html>
<html lang="en">
<head>
<meta charset="utf-8">
<title>Morvane Equity – Business Card</title>
<link rel="stylesheet" href="https://fonts.googleapis.com/css2?family=Arimo:wght@400;700&family=Jost:wght@500&display=swap">
<style>
  :root {
    --backdrop: #6a6a6a;
    --navy: #221f68;
    --navy-light: #2a2775;
    --white: #ffffff;
    --gray-mark: #8e8e8e;
    --card-shadow: 0 3px 6px rgba(0,0,0,0.45);
  }
  * { margin: 0; padding: 0; box-sizing: border-box; }
  html, body {
    width: 1200px; height: 802px; overflow: hidden;
    background: var(--backdrop);
  }
  .stage { position: relative; width: 1200px; height: 802px; }
  .card {
    position: absolute; top: 274px;
    width: 443px; height: 264px;
    box-shadow: var(--card-shadow);
    overflow: hidden;
  }
  .card-front { left: 136px; background: var(--navy); }
  .card-back { left: 624px; background: var(--white); }

  .front-shapes { position: absolute; inset: 0; }

  .front-company {
    position: absolute; left: 26px; top: 44px;
    font-family: "Jost", sans-serif; font-weight: 500;
    font-size: 17px; letter-spacing: 1.2px;
    color: var(--white); white-space: nowrap;
  }
  .person { position: absolute; left: 24px; top: 123px; color: var(--white); font-family: "Arimo", Arial, sans-serif; }
  .person-name { font-weight: 700; font-size: 15.5px; letter-spacing: 0.3px; line-height: 1; }
  .person-title { font-size: 12.5px; margin-top: 3px; }
  .contact { position: absolute; left: 24px; color: var(--white); font-family: "Arimo", Arial, sans-serif; font-size: 12.5px; line-height: 15.6px; }
  .contact-phone { top: 163px; display: flex; align-items: center; gap: 3px; }
  .contact-phone svg { width: 8px; height: 11px; }
  .contact-address { top: 193px; }

  .back-lockup {
    position: absolute; left: 0; right: 0; top: 58px;
    display: flex; flex-direction: column; align-items: center; gap: 22px;
  }
  .back-square { width: 70px; height: 70px; background: var(--navy); }
  .back-name {
    font-family: "Jost", sans-serif; font-weight: 500;
    font-size: 23px; letter-spacing: 1.5px; color: var(--navy);
    white-space: nowrap;
  }
</style>
</head>
<body>
<main class="stage">
  <section class="card card-front" aria-label="Business card front">
    <svg class="front-shapes" viewBox="0 0 443 264" width="443" height="264" aria-hidden="true">
      <polygon points="222,0 400,0 443,0 443,264 222,264 150,132" fill="var(--navy-light)"/>
      <polygon points="385,0 443,0 443,264 405,264 443,100" fill="var(--white)" opacity="0"/>
      <polygon points="388,0 443,0 443,264 388,264 430,132" fill="var(--white)"/>
      <rect class="front-square" x="237" y="77" width="118" height="118" fill="var(--gray-mark)"/>
    </svg>
    <div class="front-company">MORVANE EQUITY LLC</div>
    <div class="person">
      <div class="person-name">PETER DALBY</div>
      <div class="person-title">Portfolio Manager</div>
    </div>
    <div class="contact contact-phone">
      <svg viewBox="0 0 8 11" aria-hidden="true"><rect x="0.7" y="0.7" width="6.6" height="9.6" rx="1.2" fill="none" stroke="#fff" stroke-width="1.2"/><rect x="3" y="8" width="2" height="1" fill="#fff"/></svg>
      <span>(412) 555-0187</span>
    </div>
    <address class="contact contact-address" style="font-style:normal">
      MORVANE EQUITY LLC<br>
      2650 Birchmont Lane<br>
      Suite 300, Atlanta GA 30327
    </address>
  </section>

  <section class="card card-back" aria-label="Business card back">
    <div class="back-lockup">
      <div class="back-square" aria-hidden="true"></div>
      <div class="back-name">MORVANE EQUITY LLC</div>
    </div>
  </section>
</main>
</body>
</html>
```